Post card for annual skin cancer screening exam

We are looking to design a modern, classy, clean, but fun postcard that we will send out to patients to remind them to schedule their follow up exams for our dermatology office.

It should include our logo
http://tovimek.com/design/logo/jpg/tovimek2.jpg
http://tovimek.com/design/logo/jpg/tovimek.jpg

Address
Phone number
website

We are open to your ideas on wording, as something clever is always appreciated - though this is going to both young and elderly patients - so the message must be easy to read and clear.
Updates

Font styles to use
Serif

Colors
85cae6
3176b5

Requirements
Must have
• Logo
• Office address
• Phone number
• website
• call to action message - to schedule a follow up visit

```html
<!DOCTYPE html>
<html lang="en">
<head>
<meta charset="utf-8">
<title>Tovimek Dermatology – Postcard Back</title>
<link rel="stylesheet" href="https://fonts.googleapis.com/css2?family=Arimo:ital,wght@0,400;1,700&family=EB+Garamond:ital,wght@0,400;0,600;1,400&display=swap">
<style>
  :root {
    --page-bg: #ffffff;
    --card-top: #ececed;
    --card-bottom: #ffffff;
    --brand-sky: #85cae6;
    --brand-ocean: #3176b5;
    --brand-teal: #2a8bb0;
    --address-grey: #8a8a8a;
    --body-grey: #5f6670;
  }
  html, body {
    margin: 0;
    padding: 0;
    width: 1200px;
    height: 1200px;
    overflow: hidden;
    background: var(--page-bg);
  }
  .postcard-back {
    position: absolute;
    left: 32px;
    top: 52px;
    width: 1128px;
    height: 875px;
    background: linear-gradient(155deg, var(--card-top) 0%, #f3f3f4 45%, var(--card-bottom) 70%);
    box-shadow: 4px 6px 10px rgba(0, 0, 0, 0.18);
  }
  .return-block {
    position: absolute;
    left: 54px;
    top: 58px;
    width: 400px;
    text-align: center;
  }
  .brand-mark {
    display: block;
    margin: 0 auto 22px;
  }
  .brand-name {
    font-family: "Arimo", sans-serif;
    font-weight: 400;
    font-size: 36px;
    letter-spacing: -0.5px;
    color: var(--brand-teal);
    margin: 0;
    line-height: 1;
  }
  .return-address {
    font-family: "Arimo", sans-serif;
    font-style: italic;
    font-weight: 700;
    font-size: 21px;
    line-height: 30px;
    color: var(--address-grey);
    margin: 18px 0 0;
  }
  .reminder {
    position: absolute;
    left: 500px;
    top: 470px;
    width: 560px;
    text-align: right;
    font-family: "EB Garamond", serif;
  }
  .reminder-title {
    font-size: 44px;
    font-weight: 600;
    line-height: 1.1;
    color: var(--brand-ocean);
    margin: 0;
  }
  .reminder-text {
    font-size: 25px;
    line-height: 1.35;
    color: var(--body-grey);
    margin: 16px 0 0;
  }
  .reminder-rule {
    width: 140px;
    height: 3px;
    background: var(--brand-sky);
    margin: 24px 0 22px auto;
    border: 0;
  }
  .contact-line {
    font-size: 28px;
    line-height: 1.3;
    color: var(--brand-teal);
    margin: 0;
  }
  .contact-line .label {
    font-style: italic;
    color: var(--body-grey);
  }
</style>
</head>
<body>
  <section class="postcard-back">
    <div class="return-block">
      <svg class="brand-mark" width="78" height="78" viewBox="0 0 78 78" aria-hidden="true">
        <circle cx="39" cy="39" r="37" fill="var(--brand-sky)"/>
      </svg>
      <p class="brand-name">Tovimek Dermatology</p>
      <p class="return-address">412 North Harbor Mill Road,<br>Westbrook, NY, 11592</p>
    </div>

    <div class="reminder">
      <p class="reminder-title">It’s time for your yearly skin check!</p>
      <p class="reminder-text">A quick annual exam is the best way to keep your skin healthy. Call us today to schedule your follow-up visit.</p>
      <hr class="reminder-rule">
      <p class="contact-line"><span class="label">Call</span> (516) 555-0147</p>
      <p class="contact-line"><span class="label">Visit</span> www.tovimekderm.com</p>
    </div>
  </section>
</body>
</html>
```